"Breathe & Bloom" Book Cover 5.5x8.5

Title of the book is "Breathe & Bloom"
Subtitle is "Unmasking Pricing Myths"
I've used PixelGuild on multiple occasions you can look on my Borvex page, Mark Delwitt, to see the covers I've used in the other projects I've done.
The target audience are people who have been tricked to think they can't retire because inflation, i.e. cost of living is going up so much they must work to keep up. There is no evidence of this.
And those are the people I want to reach so they can "Breathe...and Bloom."
Target Market(s)
Americans aged 55 and over who are thinking about retirement
Industry/Entity Type
Financial
Requirements
Nice to have
- Keep It Simple, Stupid is my mantra. Just make it pop out when people are browsing
Should not have
- No piggy banks. No old people sitting on a beach.

```html
<!DOCTYPE html>
<html lang="en">
<head>
<meta charset="utf-8">
<title>Breathe &amp; Bloom — Book Cover</title>
<link rel="stylesheet" href="https://fonts.googleapis.com/css2?family=Tinos&family=Arimo:ital,wght@1,700&display=swap">
<style>
  :root {
    --sky-top: #6868cc;
    --sky-mid: #4e4e9a;
    --sky-low: #2a2a55;
    --sky-base: #15152a;
    --band: #6666ff;
    --footer: #0d0e12;
    --ink: #ffffff;
    --money-light: #e6e2d0;
    --money-dark: #8c8a78;
  }
  html, body { margin: 0; padding: 0; overflow: hidden; }
  body { width: 776px; height: 1200px; }
  .cover {
    position: relative;
    width: 776px;
    height: 1200px;
    overflow: hidden;
    background: linear-gradient(180deg, var(--sky-top) 0%, var(--sky-top) 22%, var(--sky-mid) 48%, var(--sky-low) 72%, var(--sky-base) 100%);
  }
  .title-line {
    position: absolute;
    left: 0; width: 100%;
    text-align: center;
    font-family: "Tinos", serif;
    color: var(--ink);
    margin: 0;
    line-height: 1;
  }
  .title-top { top: 172px; font-size: 94px; letter-spacing: 1px; }
  .title-amp { top: 268px; font-size: 40px; font-weight: 700; }
  .title-bottom { top: 302px; font-size: 120px; letter-spacing: 1px; }
  .rules { position: absolute; left: 0; top: 272px; }
  .subtitle {
    position: absolute;
    top: 412px; left: 0; width: 100%;
    text-align: center;
    font-family: "Arimo", sans-serif;
    font-style: italic;
    font-weight: 700;
    font-size: 36px;
    color: var(--ink);
    margin: 0;
  }
  .jar-photo {
    position: absolute;
    left: 125px; top: 568px;
    width: 508px; height: 462px;
    border-radius: 40px 40px 0 0;
    background: linear-gradient(180deg, var(--money-light) 0%, #cfcab3 45%, var(--money-dark) 100%);
    opacity: 0.9;
  }
  .author-band {
    position: absolute;
    left: 0; top: 1030px;
    width: 100%; height: 82px;
    background: var(--band);
    display: flex; align-items: center; justify-content: center;
    font-family: "Tinos", serif;
    font-size: 54px;
    color: var(--ink);
    letter-spacing: 1px;
  }
  .footer {
    position: absolute;
    left: 0; top: 1112px;
    width: 100%; height: 88px;
    background: var(--footer);
  }
</style>
</head>
<body>
  <main class="cover">
    <h1 class="title">
      <span class="title-line title-top">BREATHE</span>
      <span class="title-line title-amp">&amp;</span>
      <span class="title-line title-bottom">BLOOM</span>
    </h1>
    <svg class="rules" width="776" height="12" viewBox="0 0 776 12" aria-hidden="true">
      <defs>
        <linearGradient id="rule-left" x1="0" x2="1">
          <stop offset="0" stop-color="#fff" stop-opacity="0.9"/>
          <stop offset="1" stop-color="#fff" stop-opacity="0.3"/>
        </linearGradient>
        <linearGradient id="rule-right" x1="0" x2="1">
          <stop offset="0" stop-color="#fff" stop-opacity="0.3"/>
          <stop offset="1" stop-color="#fff" stop-opacity="0.9"/>
        </linearGradient>
      </defs>
      <polygon points="166,6 305,1 305,11" fill="url(#rule-left)"/>
      <polygon points="454,1 592,6 454,11" fill="url(#rule-right)"/>
    </svg>
    <p class="subtitle">Unmasking Pricing Myths</p>
    <div class="jar-photo" role="img" aria-label="Photograph of rolled dollar bills in a clear glass jar"></div>
    <div class="author-band">MARK DELWITT</div>
    <div class="footer"></div>
  </main>
</body>
</html>
```